Tolvine Logo and business card

We need a business card and logo, we are currently using a logo that we like but would like to be a bit more streamlined. We deal with very high end clients and our business card needs to reflect that. We would love to see and hire somebody that can deliver a very MODERN, simple design. With he main front of the card to be black with either a red lettering or White to provide great contrast. I would like to have a minimalist abstract picture of a heavy machine on it but it is not a requirement ( most likely an Crane ( a little giant crane with a bucket would be perfect or maybe a vantoro 520 RX )) If it keeps in line with being a classic simple, and modern design. Letterpress is also an option where it gives it a great look and texture, the card will be printed on a thick stock. On the back there needs to be a star included somewhere on the card and design, this represents the first generation that started the company back in 1936 therefore it is a sentimental addition ( make it modern and simple)
We do not want a cheesy construction template. We do heavy site work, aka we use excavators, payloaders, off road dorn h40 trucks, very big fun toys.
There is a huge chance to get the web design as well for the winning design.
Have fun, cannot wait to see the designs!
In addition, we'd like to point out that our primary need and priority is still the BUSINESS CARD design itself. The logo has to complement the overall look of the business card, but it is secondary to the card's look. Please keep this in mind.
Thank you,
Gerald
Target Market(s)
General Contractors, upscale home owners ( house values of 1M plus)
and commercial property owners.
Projects range from $5000 to 1 million.
Industry/Entity Type
Construction
Requirements
Must have
- Star incorporated into design
Nice to have
- an abstract heavy site work machine ( pics attached) If it keeps in line with being a classic simple, and modern design.
I would like to have black and red on the design since all the lettering on the trucks is red, but i will let the designer take care of that.

```html
<!DOCTYPE html>
<html lang="en">
<head>
<meta charset="utf-8">
<title>Tolvine Industries Inc. — Business Card</title>
<link rel="stylesheet" href="https://fonts.googleapis.com/css2?family=Questrial&family=Arimo:wght@700&display=swap">
<style>
  :root {
    --page-bg: #e9e9e9;
    --card-black: #1c1c1c;
    --skyline-top: #4d4d4d;
    --skyline-mid: #2e2e2e;
    --card-white: #fbfbfb;
    --brand-red: #d5161e;
    --ink: #222222;
    --ink-soft: #3a3a3a;
  }
  * { box-sizing: border-box; margin: 0; padding: 0; }
  html, body {
    width: 1200px; height: 1200px; overflow: hidden;
    background: var(--page-bg);
    font-family: "Questrial", "Century Gothic", sans-serif;
  }
  .sheet {
    width: 1200px; height: 1200px;
    display: flex; flex-direction: column; align-items: center; justify-content: center;
    gap: 60px;
  }
  .card {
    position: relative;
    width: 840px; height: 480px;
    overflow: hidden;
    box-shadow: 0 6px 20px rgba(0,0,0,0.12);
  }

  /* Front */
  .card-front { background: var(--card-black); }
  .skyline {
    position: absolute; left: 0; top: 0; width: 100%; height: 220px;
    background: linear-gradient(180deg, var(--skyline-top) 0%, var(--skyline-mid) 55%, var(--card-black) 100%);
  }
  .front-logo {
    position: absolute; left: 430px; top: 300px;
    display: flex; align-items: center; gap: 14px;
  }
  .logo-text { display: flex; flex-direction: column; line-height: 1; color: var(--brand-red); font-weight: 400; }
  .front-logo .logo-name { font-size: 58px; letter-spacing: 1px; }
  .front-logo .logo-sub { font-size: 24px; letter-spacing: 2px; margin-top: 6px; }
  .logo-mark { width: 44px; height: 44px; background: var(--brand-red); flex: none; }

  /* Back */
  .card-back { background: var(--card-white); color: var(--ink); }
  .holder { position: absolute; left: 60px; top: 60px; }
  .holder-name {
    font-family: "Arimo", Arial, sans-serif; font-weight: 700;
    font-size: 30px; letter-spacing: 1px; color: var(--ink);
  }
  .holder-title { font-size: 19px; margin-top: 8px; color: var(--ink-soft); }
  .address {
    position: absolute; left: 60px; top: 190px;
    font-size: 17px; line-height: 1.45; color: var(--ink-soft); font-style: normal;
  }
  .heritage-star {
    position: absolute; left: 60px; bottom: 60px;
    width: 30px; height: 30px;
  }
  .back-logo {
    position: absolute; right: 60px; top: 110px;
    display: flex; align-items: center; gap: 12px;
  }
  .back-logo .logo-name { font-size: 44px; letter-spacing: 1px; }
  .back-logo .logo-sub { font-size: 18px; letter-spacing: 2px; margin-top: 4px; }
  .back-logo .logo-mark { width: 32px; height: 32px; }
  .contacts { position: absolute; left: 470px; top: 320px; list-style: none; }
  .contact { display: flex; align-items: center; gap: 14px; font-size: 19px; line-height: 1; margin-bottom: 12px; color: var(--ink); }
  .contact-icon { width: 22px; height: 22px; flex: none; }
</style>
</head>
<body>
<main class="sheet">
  <section class="card card-front" aria-label="Card front">
    <div class="skyline" role="img" aria-label="Dark silhouette of an excavator and harbour cranes along a skyline"></div>
    <div class="front-logo">
      <div class="logo-text">
        <span class="logo-name">Tolvine</span>
        <span class="logo-sub">INDUSTRIES INC.</span>
      </div>
      <span class="logo-mark" aria-hidden="true"></span>
    </div>
  </section>

  <section class="card card-back" aria-label="Card back">
    <div class="holder">
      <p class="holder-name">GERALD HALE</p>
      <p class="holder-title">Site Work Operations Lead</p>
    </div>
    <address class="address">
      <p>14 Quarry Lane</p>
      <p>Suite 2 Northbrook</p>
      <p>Vermont</p>
    </address>
    <svg class="heritage-star" viewBox="0 0 24 24" role="img" aria-label="Star honouring the founding generation of 1936">
      <polygon points="12,1.5 14.9,8.6 22.5,9.2 16.7,14.2 18.5,21.7 12,17.7 5.5,21.7 7.3,14.2 1.5,9.2 9.1,8.6" fill="var(--brand-red)"/>
    </svg>
    <div class="back-logo">
      <div class="logo-text">
        <span class="logo-name">Tolvine</span>
        <span class="logo-sub">INDUSTRIES INC.</span>
      </div>
      <span class="logo-mark" aria-hidden="true"></span>
    </div>
    <ul class="contacts">
      <li class="contact">
        <svg class="contact-icon" viewBox="0 0 24 24" aria-hidden="true">
          <circle cx="12" cy="12" r="12" fill="var(--brand-red)"/>
          <path d="M8 6.5h2.2l1 3-1.4 1a7 7 0 0 0 3.7 3.7l1-1.4 3 1V16a1.5 1.5 0 0 1-1.6 1.5A10 10 0 0 1 6.5 8.1 1.5 1.5 0 0 1 8 6.5z" fill="#fff"/>
        </svg>
        <span>+1 8 555 014 2290</span>
      </li>
      <li class="contact">
        <svg class="contact-icon" viewBox="0 0 24 24" aria-hidden="true">
          <circle cx="12" cy="12" r="12" fill="var(--brand-red)"/>
          <rect x="8.5" y="5.5" width="7" height="13" rx="1.2" fill="#fff"/>
          <rect x="9.7" y="7" width="4.6" height="8.5" fill="var(--brand-red)"/>
        </svg>
        <span>+1 (8) 555 018 4471</span>
      </li>
      <li class="contact">
        <svg class="contact-icon" viewBox="0 0 24 24" aria-hidden="true">
          <circle cx="12" cy="12" r="12" fill="var(--brand-red)"/>
          <rect x="6" y="8" width="12" height="8.5" rx="1" fill="#fff"/>
          <path d="M6.3 8.5 12 13l5.7-4.5" fill="none" stroke="var(--brand-red)" stroke-width="1.2"/>
        </svg>
        <span>gerald.hale@tolvine.com</span>
      </li>
    </ul>
  </section>
</main>
</body>
</html>
```